(Wix) Website Design Tweaks

The site: www.LanternAndLoomly.com
(The coding must be done within Wix. I will create a duplicate website so you can gain access and begin editing.)

My website contains my preferred text and images - but it needs to look more professional. My business focuses on "Corporate Messaging" and "Marketing Communications", so the website needs to look professional, but not too corporate. My clients range from very big companies to technology startups - the look and feel should be uncluttered, professional, and modern.

I want someone to review the pages, and make changes / suggestions focused on:
1) Fonts
2) Colors
3) Layout

If you have ideas for adding additional graphics, that's fine, but they should be consistent with what I already have . . . unless you think some / all of my images need to be changed.

My site is very, very small, and only contains 5 (very short) pages. There are no sub-pages. (One page is the contact page, with almost nothing except form fields.)

If you do a good job with my site, I may be able to provide you with additional work - many of my clients need website design tweaks, after I provide the verbiage.

```html
<!DOCTYPE html>
<html lang="en">
<head>
<meta charset="utf-8">
<title>Lantern &amp; Loomly</title>
<link href="https://fonts.googleapis.com/css2?family=Montserrat:wght@400;500;600;700&display=swap" rel="stylesheet">
<style>
:root{
  --blue:#1e88e5;
  --blue-bright:#2b93ea;
  --navy:#0c1b2e;
  --ink:#1b2233;
  --text:#3a4152;
  --mist:#e9edf6;
  --white:#ffffff;
  --grey:#8a909c;
}
*{margin:0;padding:0;box-sizing:border-box}
html,body{width:1200px;height:3940px;overflow:hidden}
body{font-family:"Montserrat",sans-serif;color:var(--ink);background:var(--white);position:relative}
section,header,footer{position:absolute;left:0;width:1200px}
.abs{position:absolute}

/* nav */
.site-header{top:0;height:75px;background:var(--white)}
.brand{left:133px;top:22px;font-size:23px;font-weight:500;letter-spacing:.3px;color:var(--navy)}
.brand .accent{color:var(--blue)}
.nav{left:444px;top:0;display:flex;height:75px}
.nav a{font-size:12.5px;font-weight:500;color:var(--ink);text-decoration:none;height:75px;display:flex;align-items:center;margin-right:70px;position:relative}
.nav a.active{color:var(--blue)}
.nav a.active::after{content:"";position:absolute;left:0;right:0;bottom:0;height:3px;background:var(--blue)}

/* hero */
.hero{top:75px;height:628px;overflow:hidden}
.hero-visual{position:absolute;inset:0;background:linear-gradient(100deg,#06121f 0%,#0b2442 35%,#0f4f9c 62%,#1a86e6 82%,#33c4f2 100%)}
.hero-kicker{left:128px;top:201px;font-size:17px;letter-spacing:2px;color:var(--white);font-weight:500}
.hero-title{left:126px;top:229px;font-size:48px;line-height:42px;font-weight:700;color:var(--white)}
.hero-lede{left:128px;top:334px;font-size:15.5px;line-height:25px;color:#dfe8f4;width:450px}
.hero-arrow{top:245px}
.scroll-cue{left:590px;top:560px}

/* challenge */
.challenge{top:703px;height:436px}
.eyebrow{font-size:16px;font-weight:500;color:var(--blue);letter-spacing:.3px}
.challenge .eyebrow{left:150px;top:106px}
.challenge-title{left:148px;top:130px;font-size:44px;line-height:48px;font-weight:500;color:var(--navy)}
.challenge-title strong{color:var(--blue);font-weight:700}
.rule{height:3px;background:var(--blue)}
.challenge .rule{left:153px;top:244px;width:60px}
.challenge-copy{left:535px;top:110px;width:540px;font-size:13.5px;line-height:22px;color:var(--text)}
.challenge-copy p+p{margin-top:11px}
.btn-outline{border:2px solid var(--blue);color:var(--blue);font-size:12px;font-weight:700;display:flex;align-items:center;justify-content:center;letter-spacing:.5px}
.challenge .btn-outline{left:533px;top:282px;width:156px;height:40px}

/* help */
.help{top:1139px;height:914px;background:var(--mist)}
.center-head{left:0;width:1200px;text-align:center}
.help .eyebrow{top:62px}
.section-title{font-size:34px;font-weight:500;color:var(--navy)}
.section-title strong{color:var(--blue);font-weight:700}
.help .section-title{top:86px}
.center-rule{left:557px;width:64px;height:3px;background:var(--blue)}
.timeline{left:598px;top:228px;width:2px;height:376px;background:var(--blue)}
.step-icon{width:94px;height:94px}
.step-title{font-size:18px;font-weight:700;color:var(--navy);letter-spacing:.2px}
.step-copy{font-size:16px;line-height:23px;color:var(--text)}
.photo-frame{background:var(--blue)}
.photo{background:linear-gradient(135deg,#d8dde4,#a9b3c0 50%,#6c7888)}

/* expertise */
.expertise{top:2053px;height:638px;background:linear-gradient(160deg,#0b1a2c 0%,#123a66 45%,#1d63b4 75%,#2b7fdc 100%)}
.expertise .eyebrow{top:65px;color:var(--white);font-size:15px}
.expertise .section-title{top:85px;color:var(--white)}
.expertise .section-title strong{color:var(--white)}
.service-grid{left:165px;top:185px;display:grid;grid-template-columns:repeat(4,211px);grid-auto-rows:148px;column-gap:12px;row-gap:14px}
.service{border:1px solid rgba(255,255,255,.22);padding:26px 26px 0;color:var(--white);font-size:14.5px;font-weight:500;line-height:18px;position:relative}
.service.featured{border:2px solid rgba(255,255,255,.85)}
.service svg{width:50px;height:50px;display:block}
.service span{position:absolute;left:26px;bottom:28px;width:170px}

/* clients */
.clients{top:2691px;height:382px}
.clients .section-title{top:62px}
.client-row{left:0;top:200px;width:1200px;height:60px}
.client{position:absolute;top:0;height:60px;display:flex;align-items:center;gap:8px;transform:translateX(-50%);font-size:17px;font-weight:600;color:#5c6370;white-space:nowrap}
.client i{display:block;width:14px;height:14px;border-radius:50%;background:#8d939d}

/* results */
.results{top:3073px;height:528px}
.results-visual{left:0;top:0;width:601px;height:528px;background:linear-gradient(140deg,#05101e 0%,#0a2646 50%,#0d3c75 100%)}
.results-panel{left:601px;top:0;width:599px;height:528px;background:var(--blue-bright)}
.results-title{left:682px;top:130px;font-size:33px;color:var(--white);font-weight:500;display:flex;align-items:center}
.results-title strong{font-weight:700;margin-left:9px}
.results-title i{display:block;width:70px;height:2px;background:var(--white);margin-left:6px}
.results-copy{left:682px;top:192px;width:410px;font-size:16px;line-height:26px;color:#eef5fd}
.results-copy p+p{margin-top:6px}
.btn-light{left:682px;top:369px;width:148px;height:40px;border:2px solid var(--white);color:var(--white);font-size:11px;font-weight:700;letter-spacing:.8px;display:flex;align-items:center;justify-content:center}

/* footer */
.site-footer{top:3601px;height:282px;background:var(--white)}
.footer-brand{left:145px;top:77px;font-size:23px;font-weight:500;color:var(--navy)}
.footer-about{left:146px;top:118px;width:260px;font-size:10px;line-height:15px;color:var(--grey)}
.col-divider{top:0;width:1px;height:270px;background:#e3e7ee}
.col-mark{width:3px;height:26px;background:#9cc6ef}
.col-head{font-size:13px;font-weight:700;color:var(--navy);letter-spacing:.3px}
.col-links{list-style:none;font-size:11.5px;color:#4a5160;line-height:28px}
.socials{left:923px;top:114px;display:flex;gap:8px}
.social{display:flex;flex-direction:column;align-items:center;gap:3px;font-size:7px;color:var(--blue);font-weight:600}
.social i{display:block;width:28px;height:28px;border-radius:50%;background:var(--blue)}
.legal{top:3883px;height:57px;background:var(--mist);display:flex;align-items:center;justify-content:center;font-size:10.5px;color:#4a5160}
</style>
</head>
<body>

<header class="site-header">
  <div class="abs brand"><span class="accent">LANTERN</span> &amp; LOOMLY</div>
  <nav class="abs nav">
    <a class="active">HOME</a><a>ABOUT US</a><a>TESTIMONIALS</a><a>TEAM</a><a>CONTACT</a>
  </nav>
</header>

<section class="hero">
  <div class="hero-visual" role="img" aria-label="Hand touching a glowing digital interface ring with business icons around the company name"></div>
  <svg class="abs hero-arrow" style="left:32px" width="36" height="70" viewBox="0 0 36 70"><path d="M32 4 L4 35 L32 66" fill="none" stroke="#fff" stroke-width="2"/></svg>
  <svg class="abs hero-arrow" style="left:1130px" width="36" height="70" viewBox="0 0 36 70"><path d="M4 4 L32 35 L4 66" fill="none" stroke="#fff" stroke-width="2"/></svg>
  <div class="abs hero-kicker">LANTERN &amp; LOOMLY</div>
  <h1 class="abs hero-title">INFORM.<br>INFLUENCE. SELL.</h1>
  <p class="abs hero-lede">In today's competitive business environment effective communication is more essential than ever before.</p>
  <svg class="abs scroll-cue" width="24" height="48" viewBox="0 0 24 48"><rect x="4" y="2" width="16" height="26" rx="8" fill="none" stroke="#fff" stroke-width="1.6"/><line x1="12" y1="8" x2="12" y2="13" stroke="#fff" stroke-width="1.6"/><path d="M7 33 L12 38 L17 33 M7 39 L12 44 L17 39" fill="none" stroke="#fff" stroke-width="1.4"/></svg>
</section>

<section class="challenge">
  <div class="abs eyebrow">WHO WE ARE</div>
  <h2 class="abs challenge-title">THE BIG<br><strong>CHALLENGE</strong></h2>
  <div class="abs rule"></div>
  <div class="abs challenge-copy">
    <p>In today's competitive business environment, effective communication is more essential than ever before. It is the foundation upon which companies are built, careers are propelled, and knowledge is imparted.</p>
    <p>Effective communication is critical - without it, misunderstandings arise, errors occur, and business goals are frustrated. In short, effective communication is the key driver of long-term business and professional success.</p>
  </div>
  <div class="abs btn-outline">LEARN MORE</div>
</section>

<section class="help">
  <div class="abs center-head eyebrow">WHY WE ARE</div>
  <h2 class="abs center-head section-title">HOW CAN <strong>WE HELP</strong></h2>
  <div class="abs center-rule" style="top:138px"></div>
  <div class="abs timeline"></div>

  <div class="abs step-title" style="left:145px;top:250px">HELP INVIDUAL &amp; ORGANIZATION</div>
  <p class="abs step-copy" style="left:146px;top:287px;width:370px">At Lantern &amp; Loomly, we help individuals and organizations “get what they want” through clear and persuasive communication.</p>
  <svg class="abs step-icon" style="left:552px;top:279px" viewBox="0 0 94 94"><circle cx="47" cy="47" r="44" fill="var(--mist)"/><path d="M47 3 A44 44 0 1 1 8 68" fill="none" stroke="var(--blue)" stroke-width="4"/><circle cx="47" cy="47" r="36" fill="#fff"/><g fill="none" stroke="#1a3a66" stroke-width="1.6"><circle cx="47" cy="30" r="4"/><circle cx="32" cy="45" r="4"/><circle cx="62" cy="45" r="4"/><circle cx="47" cy="60" r="4"/><circle cx="47" cy="45" r="2"/><path d="M41 30 H35 M53 30 H59 M40 60 H34 M54 60 H60"/></g></svg>
  <div class="abs photo-frame" style="left:702px;top:205px;width:370px;height:262px"></div>
  <div class="abs photo" style="left:690px;top:193px;width:370px;height:262px" role="img" aria-label="Presenter at a flip chart coaching a small business team"></div>

  <div class="abs photo-frame" style="left:146px;top:542px;width:372px;height:262px"></div>
  <div class="abs photo" style="left:158px;top:532px;width:370px;height:262px" role="img" aria-label="Professionals seated in a row attending a training session"></div>
  <svg class="abs step-icon" style="left:557px;top:606px" viewBox="0 0 94 94"><circle cx="47" cy="47" r="44" fill="var(--mist)"/><path d="M8 26 A44 44 0 0 1 91 47" fill="none" stroke="#1a3a66" stroke-width="4"/><circle cx="47" cy="47" r="36" fill="#fff"/><g fill="none" stroke="#1a3a66" stroke-width="1.6"><rect x="42" y="28" width="24" height="16"/><path d="M46 40 L52 34 L56 38 L62 32"/><circle cx="34" cy="38" r="3"/><path d="M31 44 V60 M37 44 V60 M38 44 L44 40"/><circle cx="44" cy="54" r="3"/><circle cx="54" cy="54" r="3"/><circle cx="64" cy="54" r="3"/><path d="M40 64 Q44 58 48 64 M50 64 Q54 58 58 64 M60 64 Q64 58 68 64"/></g></svg>
  <div class="abs step-title" style="left:683px;top:610px">COACHING &amp; TRAINING</div>
  <p class="abs step-copy" style="left:683px;top:645px;width:370px">Our consulting, coaching, and training services help clients achieve targeted business objectives, with an emphasis on informing, influencing, and selling.</p>
</section>

<section class="expertise">
  <div class="abs center-head eyebrow">WHAT WE DO</div>
  <h2 class="abs center-head section-title">OUR <strong>EXPERTISE</strong></h2>
  <div class="abs center-rule" style="top:140px;background:var(--blue-bright)"></div>
  <div class="abs service-grid">
    <div class="service featured"><svg viewBox="0 0 50 50" fill="none" stroke="#fff" stroke-width="1.5"><rect x="18" y="6" width="28" height="18"/><circle cx="11" cy="14" r="4"/><path d="M8 20 V34 M14 20 V34 M15 22 L22 18"/><circle cx="20" cy="36" r="3"/><circle cx="30" cy="36" r="3"/><circle cx="40" cy="36" r="3"/><path d="M15 46 Q20 40 25 46 M25 46 Q30 40 35 46 M35 46 Q40 40 45 46"/></svg><span>Sales Training</span></div>
    <div class="service"><svg viewBox="0 0 50 50" fill="none" stroke="#fff" stroke-width="1.5"><circle cx="25" cy="25" r="8"/><circle cx="8" cy="10" r="4"/><circle cx="25" cy="6" r="4"/><circle cx="42" cy="10" r="4"/><circle cx="8" cy="40" r="4"/><circle cx="25" cy="44" r="4"/><circle cx="42" cy="40" r="4"/><path d="M11 13 L19 20 M25 10 V17 M39 13 L31 20 M11 37 L19 30 M25 40 V33 M39 37 L31 30"/></svg><span>Marketing Collateral</span></div>
    <div class="service"><svg viewBox="0 0 50 50" fill="none" stroke="#fff" stroke-width="1.5"><rect x="8" y="6" width="30" height="22"/><path d="M13 22 L20 15 L25 19 L32 12"/><circle cx="36" cy="30" r="4"/><path d="M30 46 V38 Q36 33 42 38 V46"/><path d="M23 28 V42"/></svg><span>Presentation Skills Training</span></div>
    <div class="service"><svg viewBox="0 0 50 50" fill="none" stroke="#fff" stroke-width="1.5"><rect x="6" y="6" width="34" height="24"/><path d="M18 30 V37 M28 30 V37 M13 37 H33"/><path d="M11 13 H25 M11 19 H30"/><circle cx="38" cy="34" r="6"/><path d="M35 34 L37 36 L41 32"/></svg><span>Corporate &amp; Website Messaging</span></div>
    <div class="service"><svg viewBox="0 0 50 50" fill="none" stroke="#fff" stroke-width="1.5"><path d="M6 8 H32 V26 H16 L10 31 V26 H6 Z"/><path d="M20 30 V36 H36 L42 41 V36 H46 V18 H36"/><path d="M11 15 H27 M11 20 H22"/></svg><span>Keynote Speeches</span></div>
    <div class="service"><svg viewBox="0 0 50 50" fill="none" stroke="#fff" stroke-width="1.5"><path d="M14 44 V34 Q6 28 8 18 Q11 6 25 6 Q39 6 40 20 L44 28 H40 V36 H32 V44"/><circle cx="24" cy="20" r="7"/><path d="M20 16 L28 24 M28 16 L20 24"/></svg><span>Elevator Pitches</span></div>
    <div class="service"><svg viewBox="0 0 50 50" fill="none" stroke="#fff" stroke-width="1.5"><rect x="18" y="4" width="18" height="38"/><rect x="36" y="16" width="8" height="26"/><path d="M22 10 H32 M22 16 H32 M22 22 H32 M22 28 H32 M22 34 H32"/><circle cx="11" cy="34" r="7"/><path d="M11 30 V38 M9 32 H13"/><path d="M4 44 H46"/></svg><span>Venture Capital Presentations &amp; Decks</span></div>
    <div class="service"><svg viewBox="0 0 50 50" fill="none" stroke="#fff" stroke-width="1.5"><path d="M6 8 H30 V24 H14 L8 29 V24 H6 Z"/><path d="M20 18 H46 V36 H42 V42 L36 36 H20 Z"/><path d="M25 25 H40 M25 30 H36"/></svg><span>Convention &amp; Trade Show Messaging</span></div>
  </div>
</section>

<section class="clients">
  <h2 class="abs center-head section-title">OUR <strong>CLIENTS</strong></h2>
  <div class="abs center-rule" style="top:114px"></div>
  <div class="abs client-row">
    <svg class="abs" style="left:62px;top:18px" width="36" height="24" viewBox="0 0 36 24"><path d="M34 12 H3 M12 3 L3 12 L12 21" fill="none" stroke="#6aa9df" stroke-width="2"/></svg>
    <div class="client" style="left:171px"><i></i>Orchard Co</div>
    <div class="client" style="left:329px">Telvane</div>
    <div class="client" style="left:494px">Indigo Troupe</div>
    <div class="client" style="left:660px">Harbor Docks</div>
    <div class="client" style="left:835px">Netwave</div>
    <div class="client" style="left:995px">Meridian Trust</div>
    <svg class="abs" style="left:1071px;top:18px" width="36" height="24" viewBox="0 0 36 24"><path d="M2 12 H33 M24 3 L33 12 L24 21" fill="none" stroke="#6aa9df" stroke-width="2"/></svg>
  </div>
</section>

<section class="results">
  <div class="abs results-visual" role="img" aria-label="Finger touching a glowing rising arrow above a digital bar chart"></div>
  <div class="abs results-panel"></div>
  <h2 class="abs results-title">THE<strong>RESULTS</strong><i></i></h2>
  <div class="abs results-copy">
    <p>Whatever the message, and whatever the medium, we help clients establish a connection, make an impression, and drive audiences toward a predetermined course of action.</p>
    <p>This results in clear messaging, captivated audiences, and increased sales.</p>
  </div>
  <div class="abs btn-light">LEARN MORE</div>
</section>

<footer class="site-footer">
  <div class="abs footer-brand">LANTERN &amp; LOOMLY</div>
  <p class="abs footer-about">Lantern &amp; Loomly partners with publishers to maximize their revenue potential by providing scalable and precision demand generation services.</p>

  <div class="abs col-divider" style="left:450px"></div>
  <div class="abs col-mark" style="left:448px;top:82px"></div>
  <div class="abs col-head" style="left:495px;top:88px">NAVIGATION</div>
  <ul class="abs col-links" style="left:495px;top:112px"><li>Home</li><li>About Us</li><li>Our Services</li></ul>

  <div class="abs col-divider" style="left:680px"></div>
  <div class="abs col-mark" style="left:678px;top:82px"></div>
  <div class="abs col-head" style="left:728px;top:88px">RESOURCES</div>
  <ul class="abs col-links" style="left:730px;top:112px"><li>Testimonials</li><li>Team</li><li>Contact Us</li></ul>

  <div class="abs col-divider" style="left:905px"></div>
  <div class="abs col-mark" style="left:903px;top:82px"></div>
  <div class="abs col-head" style="left:923px;top:88px">FOLLOW US</div>
  <div class="abs socials">
    <div class="social"><i></i>Pagebook</div>
    <div class="social"><i></i>Chirrup</div>
    <div class="social"><i></i>Reeltime</div>
    <div class="social"><i></i>Snapframe</div>
  </div>
</footer>

<div class="abs legal" style="left:0;width:1200px">© 2022 Lantern &amp; Loomly | All Rights Reserved</div>

</body>
</html>
```